Harlowe plumbing business cards

Want a functional designed for my business cards using my logo

Company Name- Harlowe Plumbing, Heating & Water Systems
Name- Marcus Harlowe
Title- Vice President
Cell- 555-318-7426
Email- Harloweplumbing@mailbrook.net
Business address-
PO Box 37
Fenwick Mill, MD 21999

Industry/Entity Type

Plumbing

```html
<!DOCTYPE html>
<html lang="en">
<head>
<meta charset="utf-8">
<title>Harlowe Plumbing — Business Cards</title>
<link rel="stylesheet" href="https://fonts.googleapis.com/css2?family=Source+Sans+3:wght@400;600;700&display=swap">
<style>
  :root {
    --bg: #1c1c1d;
    --card-top: #333335;
    --card-bottom: #262628;
    --blue: #1f7fc8;
    --blue-light: #9fb8e0;
    --white: #ffffff;
    --muted: #dcdde0;
  }
  * { box-sizing: border-box; margin: 0; padding: 0; }
  html, body { width: 1200px; height: 900px; overflow: hidden; }
  body {
    background: var(--bg);
    font-family: "Source Sans 3", sans-serif;
    position: relative;
  }
  .card {
    position: absolute;
    width: 700px;
    height: 400px;
    border-radius: 30px;
    overflow: hidden;
    background: linear-gradient(160deg, var(--card-top), var(--card-bottom));
    box-shadow: 0 18px 40px rgba(0,0,0,.55);
  }
  .card--front { left: 110px; top: 40px; }
  .card--back { left: 390px; top: 460px; }

  .front-swoosh { position: absolute; inset: 0; width: 100%; height: 100%; }
  .front-brand {
    position: absolute;
    left: 0; right: 0; top: 70px;
    text-align: center;
    z-index: 1;
  }
  .brand-name {
    font-size: 46px;
    font-weight: 600;
    color: var(--blue);
    letter-spacing: .5px;
    line-height: 1;
  }
  .brand-tagline {
    margin-top: 8px;
    font-size: 24px;
    color: var(--white);
    letter-spacing: .4px;
  }
  .front-phone {
    margin-top: 12px;
    font-size: 32px;
    color: var(--blue);
    letter-spacing: 1px;
    line-height: 1.1;
  }

  .person {
    position: absolute;
    left: 60px; top: 160px;
  }
  .person-name {
    font-size: 34px;
    color: var(--white);
    font-weight: 400;
    line-height: 1;
  }
  .person-name b { font-weight: 700; }
  .person-title {
    margin-top: 4px;
    font-size: 19px;
    color: var(--blue);
    padding-left: 12px;
  }
  .divider {
    position: absolute;
    left: 345px; top: 100px;
    width: 2px; height: 120px;
    background: var(--blue);
  }
  .contacts {
    position: absolute;
    left: 370px; top: 104px;
    list-style: none;
  }
  .contacts li {
    display: flex;
    align-items: center;
    gap: 10px;
    font-size: 18px;
    color: var(--muted);
    height: 36px;
  }
  .contacts svg { width: 18px; height: 18px; flex: none; }
  .back-brand {
    position: absolute;
    right: 40px; bottom: 44px;
    display: flex;
    align-items: center;
    gap: 10px;
    font-size: 22px;
    font-weight: 600;
    color: var(--blue);
  }
  .back-brand .mark {
    width: 16px; height: 16px;
    background: var(--blue-light);
  }
</style>
</head>
<body>

  <section class="card card--front" aria-label="Card front">
    <svg class="front-swoosh" viewBox="0 0 700 400" preserveAspectRatio="none" aria-hidden="true">
      <path d="M0 400 C 200 315, 430 262, 700 250 L700 400 Z" fill="var(--blue-light)"/>
      <path d="M22 400 C 215 326, 440 274, 700 263 L700 400 Z" fill="var(--blue)"/>
    </svg>
    <div class="front-brand">
      <div class="brand-name">Harlowe Plumbing</div>
      <div class="brand-tagline">Heating &amp; Water Systems</div>
      <div class="front-phone">555.204.6193</div>
    </div>
  </section>

  <section class="card card--back" aria-label="Card back">
    <div class="person">
      <div class="person-name">Marcus <b>Harlowe</b></div>
      <div class="person-title">Vice President</div>
    </div>
    <div class="divider"></div>
    <ul class="contacts">
      <li>
        <svg viewBox="0 0 24 24" aria-hidden="true"><path fill="var(--blue)" d="M6.6 10.8a15.1 15.1 0 0 0 6.6 6.6l2.2-2.2a1 1 0 0 1 1-.25 11.4 11.4 0 0 0 3.6.6 1 1 0 0 1 1 1V20a1 1 0 0 1-1 1A17 17 0 0 1 3 4a1 1 0 0 1 1-1h3.5a1 1 0 0 1 1 1c0 1.25.2 2.45.6 3.6a1 1 0 0 1-.25 1z"/></svg>
        555-318-7426
      </li>
      <li>
        <svg viewBox="0 0 24 24" aria-hidden="true"><rect x="2" y="5" width="20" height="14" rx="1.5" fill="var(--blue)"/><path d="M3 6l9 7 9-7" stroke="var(--card-top)" stroke-width="1.6" fill="none"/></svg>
        Harloweplumbing@mailbrook.net
      </li>
      <li>
        <svg viewBox="0 0 24 24" aria-hidden="true"><path fill="var(--blue)" d="M12 2a7 7 0 0 0-7 7c0 5 7 13 7 13s7-8 7-13a7 7 0 0 0-7-7zm0 9.5A2.5 2.5 0 1 1 12 6.5a2.5 2.5 0 0 1 0 5z"/></svg>
        PO Box 37, Fenwick Mill, MD 21999
      </li>
    </ul>
    <div class="back-brand">
      <span class="mark"></span>
      Harlowe Plumbing
    </div>
  </section>

</body>
</html>
```